Professional Company Corporate Profile Brochure

Main Criteria for A4 size Corporate Profile
• Professional grade with imagery/photos – I think Portrait is best
• Imagery and Graphics - Valdrel specific – not too corporate – we are a Commercial Builder BUT also to have a level of professionalism.
• Essential to have the ability to edit/format/reconfigure to suit our needs for each client.
• Examples of some I have downloaded are attached – we need to find a happy medium between these 2
• Table of contents, Some Text and Graphic images, some of our images, plus some stock images and aspirational messages plus Project specific items
• Ultimate idea is for readers to choose to “skim through” and get a sense of who we are by imagery and top line text – or if preferred they can read through the more complex data fields and get a more detailed overview. – but it is essential we can get the message across of who we are and what services we offer through both mediums
• Review our website https://valdrel.com.au/ to see more of who we are
• Attached is an outline of what I consider should be the main points – by page - also attached 2 other companies documents I sourced off the internet which could be of assistance
Target Market(s)
Commercial Clients in Australia
Industry/Entity Type
Commercial Construction and Building Maintenance
Font styles to use
Other font styles liked:
- as per website
Colors
Designer to choose colors to be used in the design.
Requirements
Must have
- Table of contents, Some Text and Graphic images, some of our images, plus some stock images and aspirational messages plus Project specific items
Nice to have
- Carry on existing company themes as per website. www.valdrel.com.au As many as you think may convince us to go with you
Should not have
- Must be Professional and sell Valdrel

```html
<!DOCTYPE html>
<html lang="en">
<head>
<meta charset="utf-8">
<title>Valdrel Capability Statement</title>
<link href="https://fonts.googleapis.com/css2?family=Oswald:wght@400;500;600&family=Poppins:wght@400;500;600;700&family=Open+Sans:wght@400;700&display=swap" rel="stylesheet">
<style>
:root{
  --red:#dc2626;
  --charcoal:#2f323b;
  --white:#ffffff;
  --ink:#1f1f24;
  --grey:#e6e6e6;
  --backdrop:#ececea;
}
*{box-sizing:border-box;margin:0;padding:0}
html,body{width:935px;height:1200px;overflow:hidden;background:var(--backdrop)}
.canvas{position:relative;width:935px;height:1200px}
.page{position:absolute;width:372px;height:526px;background:var(--white);overflow:hidden;box-shadow:0 2px 6px rgba(0,0,0,.25)}
.abs{position:absolute}
.photo{position:absolute}

/* cover */
.cover{left:77px;top:44px;background:var(--red)}
.cover-title{left:0;width:100%;top:40px;text-align:center;font:500 27px/1 'Oswald',sans-serif;color:var(--white)}
.cover-photo{left:0;top:130px;width:372px;height:272px;background:linear-gradient(160deg,#fafafa 0%,#d9dcdf 55%,#9aa0a6 100%);clip-path:polygon(0 58%,20% 58%,52% 10%,100% 0,100% 100%,0 100%)}
.cover-band{left:0;top:402px;width:372px;height:60px;background:var(--charcoal)}
.brand{left:0;width:100%;top:416px;text-align:center;font:600 24px/1 'Oswald',sans-serif;color:var(--white);letter-spacing:.5px}
.url-tag{left:278px;top:452px;width:80px;height:18px;background:var(--white);font:600 5.5px/18px 'Poppins',sans-serif;color:var(--ink);display:flex;align-items:center;gap:4px;padding-left:6px}
.contact-row{left:0;top:489px;width:100%;display:flex;justify-content:space-around;padding:0 30px 0 40px;font:600 5px/1.3 'Poppins',sans-serif;color:var(--white)}
.contact-item{display:flex;align-items:center;gap:6px}

/* contents */
.contents{left:475px;top:44px}
.toc-label{left:40px;top:25px;width:105px;height:27px;background:var(--red);color:var(--white);font:400 10px/27px 'Oswald',sans-serif;text-align:center}
.side-grey{left:237px;top:0;width:135px;height:204px;background:var(--grey)}
.side-photo{left:237px;top:204px;width:135px;height:322px;background:linear-gradient(200deg,#3b3b3b 0%,#b91c1c 35%,#1a1a1a 60%,#d32f2f 80%,#111 100%)}
.toc-list{list-style:none}
.toc-item{position:absolute;left:40px;display:flex;align-items:center;gap:11px;font:700 5.2px/1.3 'Poppins',sans-serif;color:var(--ink);width:150px}
.toc-num{flex:none;width:15px;height:15px;background:var(--red);color:var(--white);font:700 4.5px/15px 'Poppins',sans-serif;text-align:center}

/* about */
.about{left:76px;top:598px}
.about-accent{left:278px;top:0;width:94px;height:94px;background:var(--red)}
.about-photo{left:205px;top:42px;width:144px;height:164px;background:linear-gradient(180deg,#f4f4f4 0%,#e3e3e1 70%,#c9c4bd 100%)}
.body-copy{font:400 6px/1.26 'Poppins',sans-serif;color:var(--ink);text-align:justify}
.body-copy p+p{margin-top:6px}
.about-intro{left:41px;top:47px;width:139px}
.about-block{left:26px;top:233px;width:95px;height:50px;background:var(--charcoal)}
.about-photo2{left:0;top:283px;width:188px;height:243px;background:linear-gradient(90deg,#5fa8e0 0%,#e8e8e8 25%,#f0f0f0 45%,#2b6fa6 60%,#7fbbe8 100%)}
.about-detail{left:207px;top:284px;width:138px}

/* why */
.why{left:476px;top:598px}
.why-photo{left:64px;top:0;width:230px;height:100px;background:linear-gradient(180deg,#9aa0a4 0%,#e8eaeb 50%,#cfd3d5 100%)}
.why-band{left:127px;top:41px;width:245px;height:32px;background:var(--charcoal)}
.why-title{left:40px;top:124px;font:500 27px/1 'Oswald',sans-serif;color:var(--red)}
.why-icon{position:absolute;left:37px;width:47px;height:44px;background:var(--red);display:flex;align-items:center;justify-content:center}
.why-point{position:absolute;left:106px;width:220px;font:400 4.7px/10.3px 'Open Sans',sans-serif;color:#3a2a1c;text-align:justify}
.why-point h3{font:700 4.7px/8px 'Open Sans',sans-serif;color:var(--ink);letter-spacing:.3px;text-transform:uppercase}
</style>
</head>
<body>
<div class="canvas">

  <section class="page cover">
    <h1 class="abs cover-title">Capability Statement</h1>
    <div class="photo cover-photo" role="img" aria-label="White modern apartment building viewed from below"></div>
    <div class="abs cover-band"></div>
    <div class="abs brand">VALDREL</div>
    <div class="abs url-tag">
      <svg width="6" height="7" viewBox="0 0 6 7"><path d="M0 0L6 3.5 3.2 4 4.5 7 3.6 7 2.4 4.3 0 6Z" fill="#dc2626"/></svg>
      www.valdrel.com.au
    </div>
    <div class="abs contact-row">
      <div class="contact-item">
        <svg width="7" height="9" viewBox="0 0 7 9"><path d="M3.5 0A3.5 3.5 0 0 0 0 3.5C0 6 3.5 9 3.5 9S7 6 7 3.5A3.5 3.5 0 0 0 3.5 0Zm0 5A1.5 1.5 0 1 1 3.5 2a1.5 1.5 0 0 1 0 3Z" fill="#fff"/></svg>
        <span>14 Kestrel Lane<br>Balcatta, WA 6021</span>
      </div>
      <div class="contact-item">
        <svg width="6" height="9" viewBox="0 0 6 9"><rect x="0.5" y="0.5" width="5" height="8" rx="1" fill="none" stroke="#fff"/><rect x="2" y="6.5" width="2" height="0.8" fill="#fff"/></svg>
        <span>(618) 9300 4152</span>
      </div>
      <div class="contact-item">
        <svg width="10" height="7" viewBox="0 0 10 7"><rect x="0.5" y="0.5" width="9" height="6" fill="none" stroke="#fff"/><path d="M0.5 0.5L5 4 9.5 0.5" fill="none" stroke="#fff"/></svg>
        <span>admin@valdrel.com.au</span>
      </div>
    </div>
  </section>

  <section class="page contents">
    <div class="abs toc-label">TABLE OF CONTENTS</div>
    <div class="abs side-grey"></div>
    <div class="photo side-photo" role="img" aria-label="Tall tower facade with red panels seen looking upward"></div>
    <ol class="toc-list">
      <li class="toc-item" style="top:121px"><span class="toc-num">1.</span>Lorem ipsum dolor sit amet, consectetur adipiscing elit.</li>
      <li class="toc-item" style="top:168px"><span class="toc-num">2.</span>Mauris malesuada tincidunt purus.</li>
      <li class="toc-item" style="top:207px"><span class="toc-num">3.</span>Etiam ut tortor orci. Cras magna lorem,</li>
      <li class="toc-item" style="top:246px"><span class="toc-num">4.</span>tempor eu elit a, placerat faucibus est.</li>
      <li class="toc-item" style="top:286px"><span class="toc-num">5.</span>Donec mauris enim, semper sit amet</li>
      <li class="toc-item" style="top:325px"><span class="toc-num">6.</span>dolor sed, tincidunt condimentum leo.</li>
      <li class="toc-item" style="top:364px"><span class="toc-num">7.</span>Nunc ut dignissim arcu, vitae interdum augue.</li>
      <li class="toc-item" style="top:404px"><span class="toc-num">8.</span>dolor sed, tincidunt condimentum leo.</li>
    </ol>
  </section>

  <section class="page about">
    <div class="abs about-accent"></div>
    <div class="photo about-photo" role="img" aria-label="Bright white interior with a wire chair, timber side table and framed print"></div>
    <div class="abs body-copy about-intro">
      <p>Established in 2007, Valdrel is a family business that has grown to become a trusted partner for a diverse range of businesses and government agencies across metropolitan, regional and remote areas of Western Australia.<br>We partner with our clients to assist them in achieving their goals through the provision of high-quality work that is delivered on-time and on-budget.</p>
      <p>Our Managing director, Daniel Reeve, is a registered builder with over 24 years' experience in the industry. Daniel oversees all projects and is supported by a competent team of experienced administrative professionals, qualified tradespeople and preapproved subcontractors.</p>
    </div>
    <div class="abs about-block"></div>
    <div class="photo about-photo2" role="img" aria-label="Apartment facade with glass balconies against a blue sky"></div>
    <div class="abs body-copy about-detail">
      <p>Delivering quality outcomes on construction projects and providing reliable and timely maintenance work has cemented Valdrel's position with our clients as a preferred supplier with a reputation for safety, quality, and reliability.</p>
      <p style="margin-top:15px">Long-term contracts and partnerships with companies such as Westgrid Energy and The State Treasury Office, who hold Valdrel in high regard, are a testimony to the quality of our team and the services we provide</p>
    </div>
  </section>

  <section class="page why">
    <div class="photo why-photo" role="img" aria-label="White steel and glass roof structure seen from below"></div>
    <div class="abs why-band"></div>
    <h2 class="abs why-title">Why Valdrel</h2>

    <div class="why-icon" style="top:203px">
      <svg width="26" height="26" viewBox="0 0 26 26" fill="none" stroke="#fff" stroke-width="1.1"><rect x="2" y="4" width="22" height="19" rx="1.5"/><path d="M2 9h22M7 2v4M19 2v4"/><circle cx="7" cy="13" r="1.2"/><circle cx="11" cy="13" r="1.2"/><circle cx="15" cy="13" r="1.2"/><circle cx="19" cy="13" r="1.2"/><circle cx="7" cy="18" r="1.2"/><circle cx="11" cy="18" r="1.2"/><circle cx="15" cy="18" r="1.2"/></svg>
    </div>
    <div class="why-point" style="top:197px">
      <h3>Here for the long term</h3>
      Valdrel has been a trusted partner in the commercial building and maintenance industry since 2007 and we value and maintain long-term relationships with all of our stakeholders. We invest heavily in our systems, people and technology for the future and our presence in the industry is growing.
    </div>

    <div class="why-icon" style="top:261px">
      <svg width="26" height="26" viewBox="0 0 26 26" fill="none" stroke="#fff" stroke-width="1.1"><circle cx="13" cy="13" r="10"/><circle cx="13" cy="13" r="7" stroke-dasharray="2 2"/><path d="M13 8v5l3 2"/><path d="M21 4l2 3-3 1"/></svg>
    </div>
    <div class="why-point" style="top:250px">
      <h3>Meeting your deadlines</h3>
      Our focus on systems, people and technology mean we are flexible and agile enough to deliver work on tight time frames while guaranteeing quality results. We work closely with our clients to ensure we fully understand specific site requirements and time constraints so that we can deliver on time with minimal disruption to the client's day-to-day operations delivering a high level of service and quality.
    </div>

    <div class="why-icon" style="top:318px">
      <svg width="26" height="26" viewBox="0 0 26 26" fill="none" stroke="#fff" stroke-width="1.1"><path d="M10 5h12a2 2 0 0 1 2 2v7a2 2 0 0 1-2 2h-1v3l-3-3h-2"/><path d="M3 10h12a2 2 0 0 1 2 2v6a2 2 0 0 1-2 2H9l-4 3v-3H3a2 2 0 0 1-1-2v-6a2 2 0 0 1 1-2Z"/><path d="M6 15h8M6 17.5h5"/></svg>
    </div>
    <div class="why-point" style="top:311px">
      <h3>Good communication</h3>
      Our people, with the support of our technology systems, prioritise communication and transparency at all levels of our operation to ensure our clients are kept up-to-date from quote to completion of works.
    </div>

    <div class="why-icon" style="top:376px">
      <svg width="26" height="26" viewBox="0 0 26 26" fill="none" stroke="#fff" stroke-width="1.1"><path d="M13 2l9 3v7c0 6-4 10-9 12-5-2-9-6-9-12V5Z"/><path d="M13 5l6 2v5c0 4-3 7-6 8.5-3-1.5-6-4.5-6-8.5V7Z"/><path d="M9.5 13l2.5 2.5 4.5-5"/></svg>
    </div>
    <div class="why-point" style="top:365px">
      <h3>Serious about safety</h3>
      Safety is, and has always been, our number one priority. We have built a strong company-wide culture that balances safety and quality in every aspect of our operations. We also maintain an Occupational Health and Safety ISO 45001 certification and require CM3 certification for contractors, approved by Valdrel, who perform work on our behalf.
    </div>

    <div class="why-icon" style="top:434px">
      <svg width="26" height="26" viewBox="0 0 26 26" fill="none" stroke="#fff" stroke-width="1.1"><path d="M13 3l1.8 3.6 4 .6-2.9 2.8.7 4-3.6-1.9-3.6 1.9.7-4-2.9-2.8 4-.6Z"/><path d="M2 13l4 5 3 2h4M24 13l-4 5-3 2h-4M5 24l4-4M21 24l-4-4"/></svg>
    </div>
    <div class="why-point" style="top:426px">
      <h3>Higher quality work output</h3>
      All of the work we undertake is completed to a quality that meets and exceeds client expectations. Our commitment to our people ensures consistent quality results are achieved. This commitment includes first class professional development and training, quality systems and pre-qualified contractors.
    </div>
  </section>

</div>
</body>
</html>
```